Create packaging for an innovative ear wax removal product

We are seeking a fresh design look for an innovative ear wax removal product that will appeal strongly to millennials. The images provided include packshots of existing concepts for reference. The copy can remain the same and we're happy with the hierarchy of messaging. What we need is a fresh presentation/look for the design since the current designs are considered to conventional/traditional versus more contemporary retail packaging found in US retailers.

1. GENERAL INFO
Brand: Use the placeholder "Velmora"
Positioning: Velmora produces high quality otoscopes for safe use at home by adults and families.
Deliverables: 3D packshot featuring front and side
Timing: We will be reviewing designs as they come in. Nov 4th is our deadline but the sooner designs are posted the better.

2. PRODUCT SPECIFIC INFO
Product Name: Ear Wax Removal System
Description: Ear cleanliness is important to ensure the best hearing, balance, and to prevent infection. The otoscope's advanced wireless control safety technology allows the user to view and safely clean the ear canal with ease, for routine clearing of ear wax. It's also a great tool to check your mouth, nose, hair, skin, and your pets.
Pellmore consumer: Primary = Millennials, Females aged 25-45 with young kids; Secondary = Adults 20-70
Images: Some images provided. Feel free to use AI and stock imagery.
Text: Use with the existing text. Can be same, similar or different fonts/styles.

3. EXECUTION GUIDELINES
Must be an impactful design that will grab attention at retail
Should have a contemporary look
Design should be high quality, stylish and convey ease of use, trust/safety, efficiency, effectiveness
Design should sell benefits and features in a concise compelling way (messaging hierarchy is important)
Use a combination of product and lifestyle images
Include placeholder "Velmora" logo. Ok to change color.
Dimensions of existing box (W93mm x H170mm x D31mm)
Contents:
(1) Otoscope with Cap
(2) Silicone Ear Spoons
(1) USB charging Cable
(1) Manual

Pellmore Market(s)

Primary = Millennials, 25-45 yrs, with young kids

Industry/Entity Type

Ear care. Packaging is for US retail stores, such as Stormfield, Pellmore, Vale Cure, QLN, Hollbrooks

Font styles to use
Sans Serif

Requirements
Must have
• See description
Nice to have
• See description

```html
<!DOCTYPE html>
<html lang="en">
<head>
<meta charset="utf-8">
<title>Velmora Ear Wax Removal System – Carton Dieline</title>
<link href="https://fonts.googleapis.com/css2?family=Open+Sans:ital,wght@0,400;0,500;1,800&family=Roboto+Condensed:wght@300;400&display=swap" rel="stylesheet">
<style>
  :root {
    --teal: #00aebb;
    --ink: #1c1c1c;
    --paper: #ffffff;
    --cut: #d6185e;
  }
  html, body { margin: 0; padding: 0; overflow: hidden; background: var(--paper); }
  .canvas { width: 901px; height: 1200px; display: block; }
  .brand-name { font-family: "Open Sans", sans-serif; font-weight: 500; fill: var(--paper); }
  .headline { font-family: "Open Sans", sans-serif; font-weight: 800; font-style: italic; }
  .headline .word-ear { fill: var(--paper); }
  .headline .word-wax { fill: var(--teal); }
  .tagline { font-family: "Open Sans", sans-serif; font-weight: 400; fill: var(--paper); }
  .body-copy { font-family: "Roboto Condensed", sans-serif; font-weight: 300; fill: var(--paper); }
  .cut-line { fill: none; stroke: var(--cut); stroke-width: 2; stroke-linejoin: round; }
  .panel-teal { fill: var(--teal); }
  .panel-dark { fill: var(--ink); }
  .feature-chevron { fill: none; stroke: var(--paper); stroke-width: 2; }
  .content-thumb { stroke: var(--paper); stroke-width: 2; }
</style>
</head>
<body>
<svg class="canvas" viewBox="320 1085 1020 1050" preserveAspectRatio="xMidYMid meet" xmlns="http://www.w3.org/2000/svg">
  <defs>
    <radialGradient id="ear-tone" cx="0.5" cy="0.45" r="0.55">
      <stop offset="0" stop-color="#2a2a2a"/>
      <stop offset="1" stop-color="#1c1c1c"/>
    </radialGradient>
    <linearGradient id="device-tone" x1="0" y1="0" x2="0" y2="1">
      <stop offset="0" stop-color="#4a4a4a"/>
      <stop offset="0.5" stop-color="#222"/>
      <stop offset="1" stop-color="#0d0d0d"/>
    </linearGradient>
    <radialGradient id="thumb-tone" cx="0.35" cy="0.35" r="0.7">
      <stop offset="0" stop-color="#5a5a5a"/>
      <stop offset="1" stop-color="#0e0e0e"/>
    </radialGradient>

    <g id="front-panel">
      <rect class="panel-dark" x="0" y="0" width="348" height="578"/>
      <rect class="panel-teal" x="0" y="578" width="348" height="58"/>
      <text class="brand-name" x="174" y="58" font-size="36" text-anchor="middle">Velmora</text>
      <rect x="150" y="155" width="180" height="260" rx="90" fill="url(#ear-tone)" role="img" aria-label="Soft dark photograph of a human ear"/>
      <text class="headline" font-size="92" transform="translate(88 548) rotate(-90)" textLength="410" lengthAdjust="spacingAndGlyphs"><tspan class="word-ear">EAR </tspan><tspan class="word-wax">WAX</tspan></text>
      <text class="tagline" font-size="19" transform="translate(114 548) rotate(-90)" textLength="408" lengthAdjust="spacingAndGlyphs">VIEW AND SAFELY CLEAN YOUR EAR CANAL</text>
      <text class="body-copy" font-size="13" text-anchor="end">
        <tspan x="335" y="518">Easy wireless connection to</tspan>
        <tspan x="335" y="533">Orbphones, Orbpads, Droidex</tspan>
        <tspan x="335" y="548">phones and tablets</tspan>
      </text>
      <rect x="0" y="593" width="215" height="28" rx="4" fill="url(#device-tone)" role="img" aria-label="Product shot of the wireless otoscope with blue tip"/>
      <text class="body-copy" font-size="9" text-anchor="end">
        <tspan x="335" y="601">Contains (1) Otoscope and</tspan>
        <tspan x="335" y="611">(5) Attachments.</tspan>
      </text>
    </g>
  </defs>

  <!-- glue flap -->
  <path class="cut-line" d="M395 1292 L340 1303 L340 1918 L395 1928"/>

  <!-- top closure of first front -->
  <rect class="panel-teal" x="395" y="1180" width="348" height="112"/>
  <text class="brand-name" font-size="36" text-anchor="middle" transform="translate(569 1220) rotate(180)">Velmora</text>
  <path class="cut-line" d="M397 1180 L397 1160 Q397 1103 460 1103 L680 1103 Q741 1103 741 1160 L741 1180"/>

  <!-- first front -->
  <g class="front-face" transform="translate(395 1292)"><use href="#front-panel"/></g>

  <!-- first side: features -->
  <rect class="panel-teal" x="743" y="1292" width="115" height="636"/>
  <path class="cut-line" d="M745 1292 L745 1277 L758 1265 L760 1197 L830 1197 L848 1275 L858 1285 L858 1292"/>
  <path class="cut-line" d="M745 1928 L745 1943 L755 1953 L770 2023 L840 2023 L852 1943 L858 1935"/>
  <g class="feature-list">
    <path class="feature-chevron" d="M756 1449 L761 1454 L756 1459"/>
    <text class="body-copy" font-size="13"><tspan x="767" y="1458">Ultra thin</tspan><tspan x="767" y="1473">1080p</tspan><tspan x="767" y="1488">Otoscope</tspan><tspan x="767" y="1503">camera scope</tspan><tspan x="767" y="1518">with cleaning</tspan><tspan x="767" y="1533">tools.</tspan></text>
    <path class="feature-chevron" d="M756 1590 L761 1595 L756 1600"/>
    <text class="body-copy" font-size="13"><tspan x="767" y="1599">Easy to use</tspan><tspan x="767" y="1614">wireless</tspan><tspan x="767" y="1629">connection to</tspan><tspan x="767" y="1644">Orbphones,</tspan><tspan x="767" y="1659">Orbpads,</tspan><tspan x="767" y="1674">Droidex phones</tspan><tspan x="767" y="1689">and tabelts.</tspan></text>
    <path class="feature-chevron" d="M756 1735 L761 1740 L756 1745"/>
    <text class="body-copy" font-size="13"><tspan x="767" y="1744">Safe, Easy</tspan><tspan x="767" y="1759">and</tspan><tspan x="767" y="1774">Effective</tspan></text>
  </g>

  <!-- second front -->
  <g class="front-face" transform="translate(858 1292)"><use href="#front-panel"/></g>

  <!-- bottom closure of second front -->
  <rect class="panel-teal" x="858" y="1928" width="348" height="112"/>
  <text class="brand-name" x="1032" y="1998" font-size="36" text-anchor="middle">Velmora</text>
  <path class="cut-line" d="M861 2040 L861 2062 Q861 2118 922 2118 L1142 2118 Q1204 2118 1204 2062 L1204 2040"/>

  <!-- second side: contents -->
  <rect class="panel-teal" x="1206" y="1292" width="116" height="636"/>
  <path class="cut-line" d="M1208 1292 L1208 1277 L1218 1268 L1235 1197 L1303 1197 L1310 1280 L1322 1292"/>
  <path class="cut-line" d="M1208 1928 L1208 1940 L1218 1950 L1225 2023 L1295 2023 L1313 1945 L1322 1935"/>
  <g class="contents-gallery">
    <circle class="content-thumb" cx="1264" cy="1410" r="43" fill="url(#thumb-tone)" role="img" aria-label="Close-up of the otoscope body"/>
    <circle class="content-thumb" cx="1264" cy="1510" r="43" fill="#dcdcdc" role="img" aria-label="Otoscope shown with its cap"/>
    <circle class="content-thumb" cx="1264" cy="1610" r="43" fill="url(#thumb-tone)" role="img" aria-label="Otoscope camera tip with silicone ear spoon"/>
    <circle class="content-thumb" cx="1264" cy="1710" r="43" fill="url(#thumb-tone)" role="img" aria-label="Otoscope with USB charging cable"/>
  </g>
  <text class="body-copy" font-size="10">
    <tspan x="1218" y="1798">(1) Otoscope with Cap</tspan>
    <tspan x="1218" y="1816">(2) Silicone Ear Spoons</tspan>
    <tspan x="1218" y="1834">(1) USB charging Cable</tspan>
    <tspan x="1218" y="1852">(1)  Manual</tspan>
  </text>
</svg>
</body>
</html>
```